"Wellenhafen" private practice for physiotherapy

we are looking for a flyer design for a private practice for physiotherapy. the name of the practice is "Wellenhafen".
Treatments such as: manual therapy, manual lymphatic drainage, classic massage, sectoral alternative practitioners are offered

The flyers should be double-sided and the format DIN long (105x210 mm)

Font styles to use
Serif

Colors
0094D4
00A9DD
6FCCEA
C7EBF8
E9F6FB

Requirements
Must have
• Wellenhafen, Lindenweg 17, 04719 Lindental / Wellenhafen-praxis-beispiel.de / Tel. 03471 5820317

```html
<!DOCTYPE html>
<html lang="de">
<head>
<meta charset="utf-8">
<title>Wellenhafen – Physiotherapie</title>
<link rel="stylesheet" href="https://fonts.googleapis.com/css2?family=Montserrat:wght@400;500;800&display=swap">
<style>
  :root {
    --blue-light: #0bb4e6;
    --blue-mid: #0094ca;
    --blue-base: #0b7baf;
    --blue-deep: #034366;
    --white: #ffffff;
    --rule: #dcdcdc;
  }
  html, body {
    margin: 0;
    padding: 0;
    width: 1200px;
    height: 2400px;
    overflow: hidden;
    background: var(--blue-base);
  }
  .flyer {
    position: relative;
    width: 1200px;
    height: 2400px;
    overflow: hidden;
    font-family: "Montserrat", sans-serif;
    color: var(--white);
  }
  .backdrop {
    position: absolute;
    inset: 0;
  }
  .frame {
    position: absolute;
    left: 31px;
    top: 33px;
    width: 1114px;
    height: 2311px;
    border: 12px solid var(--white);
  }
  .wordmark {
    position: absolute;
    left: 292px;
    top: 150px;
    margin: 0;
    font-weight: 800;
    font-size: 86px;
    line-height: 1;
    letter-spacing: -1px;
  }
  .rule {
    position: absolute;
    height: 5px;
    background: var(--rule);
  }
  .rule--brand { left: 296px; top: 310px; width: 608px; }
  .rule--service { left: 457px; width: 285px; }
  .service {
    position: absolute;
    left: 0;
    width: 1200px;
    margin: 0;
    text-align: center;
    font-weight: 500;
    font-size: 80px;
    line-height: 1;
    letter-spacing: -3px;
  }
  .contact {
    position: absolute;
    left: 160px;
    margin: 0;
    font-weight: 400;
    font-size: 46px;
    line-height: 57px;
    letter-spacing: 0.5px;
  }
  .icon {
    position: absolute;
    fill: none;
    stroke: var(--white);
  }
</style>
</head>
<body>
<main class="flyer">
  <svg class="backdrop" viewBox="0 0 1240 2480" width="1200" height="2400" preserveAspectRatio="none" aria-hidden="true">
    <rect width="1240" height="2480" fill="var(--blue-base)"/>
    <polygon points="0,0 1240,0 1240,1915 0,40" fill="var(--blue-mid)"/>
    <polygon points="350,0 1240,0 1240,980" fill="var(--blue-light)"/>
    <polygon points="0,1460 920,2480 0,2480" fill="var(--blue-deep)"/>
  </svg>

  <div class="frame"></div>

  <h1 class="wordmark">WELLENHAFEN</h1>
  <div class="rule rule--brand"></div>

  <p class="service" style="top:491px">MANUELLE THERAPIE</p>
  <div class="rule rule--service" style="top:622px"></div>

  <p class="service" style="top:717px">MANUELLE LYMPH</p>
  <p class="service" style="top:804px">DRAINAGE</p>
  <div class="rule rule--service" style="top:927px"></div>

  <p class="service" style="top:1036px">PHYSIOTHERAPIE</p>
  <div class="rule rule--service" style="top:1156px"></div>

  <p class="service" style="top:1295px">SEKTORALER</p>
  <p class="service" style="top:1412px">HEILPRAKTIKER</p>
  <p class="service" style="top:1528px">PHYSIOTHERAPIE</p>
  <div class="rule rule--service" style="top:1646px"></div>

  <svg class="icon" style="left:75px;top:1852px" width="44" height="62" viewBox="0 0 44 62" aria-hidden="true">
    <path d="M22 0C9.8 0 0 9.8 0 22c0 14 22 40 22 40s22-26 22-40C44 9.8 34.2 0 22 0z" fill="var(--white)" stroke="none"/>
    <circle cx="22" cy="21" r="8" fill="var(--blue-base)" stroke="none"/>
  </svg>
  <p class="contact" style="top:1847px">Wellenhafen, Lindenweg 17<br>04719 Lindental.</p>

  <svg class="icon" style="left:82px;top:2026px" width="50" height="50" viewBox="0 0 50 50" stroke-width="3" aria-hidden="true">
    <circle cx="25" cy="25" r="22"/>
    <ellipse cx="25" cy="25" rx="10" ry="22"/>
    <line x1="25" y1="3" x2="25" y2="47"/>
    <line x1="3" y1="25" x2="47" y2="25"/>
    <path d="M7 14h36M7 36h36"/>
  </svg>
  <p class="contact" style="top:2022px">wellenhafen-praxis-beispiel.de</p>

  <svg class="icon" style="left:85px;top:2175px" width="46" height="46" viewBox="0 0 46 46" stroke-width="2.5" stroke-linejoin="round" aria-hidden="true">
    <path d="M10 3l8 10-5 5c3 7 8 12 15 15l5-5 10 8-6 7C20 42 4 26 3 9z"/>
  </svg>
  <p class="contact" style="top:2169px;left:166px">03471 5820317</p>
</main>
</body>
</html>
```